Postcard designed to acquire new customers

Need a postcard style AD to place in dentist offices and other professionals to promote our tax saving system. We will place these in dentists offices, orthodontist, optometrist, physiotherapist and all sorts of medical/dental offices. The card should highlight how they can save taxes by using our software. Our website has good information on it, and I'll include the advertising PDF that our software company produces. Our logo is a little out-dated and I've included the bonus of the winner re-making the logo so its better than it currently is.
Updates

I don't need to have any space allocated for a stamp and address. We are using this to place in offices and are for advertising purposes, not mailing. Thanks!

Reason: My apologies for not providing feedback yet, I've lost several days due to some illness and am finally back at work. I'll be going through designs today and would like the extra few days to work with many of you to create a great design. Thank you for your patience! Doyle

Reason: Again, my apologies for the delay. I will be in contact with designers this week. Thank you,

Target Market(s)

Small Business Owners in Canada

Industry/Entity Type

Health Insurance

Logo Text

Save Time, Save Money

Font styles to use
Other font styles liked:
• Easy to Read Font's

Colors

Designer to choose colors to be used in the design.

Requirements
Must have
• Must have a call to action on the postcard to sell the service. We need people to have their attention caught. A call to action could be, "You're spending too much on taxes! That's what they'll say if your business doesn't have a 789 Brookvale Outlay Plan..."
• See the PDF for other catch phrases or key information on what a Health Spending Account is. Many people don't know so I'd like to see 3-4 bullet points on the front of the postcard on what a health spending account is. See the attached PDF for that information and simplifying the information to short bullet points would be best. Here are my thoughts:
• Who should have a 789 Brookvale Outlay Plan?
• - Every business owner who is incorporated should have one.
• - Write off 100% of this QTB approved this method.
• - It is the most tax effective way to run dental, health, vision and other expenses through your company.
• - Easy to use APP for your phone, 2-day turnaround time for claims
• If you aren't using this, you're throwing tax dollars away!
• The back of the postcard would include 2 things. First, an example of the taxes you can save, and second - the different information they can send us so we can setup your account.
• First is the example of how this saves you money. Assuming a 38% personal tax rate. You will need to earn $1.62 of gross income, pay $0.62 of personal tax, which leaves you with $1.00 of after tax money to use for your personal expenses.
• The example of using a 789 Brookvale Outlay Plan, or doing nothing would need the following information.
• Comparison
• $5,000 of medical, dental, vision expenses
• Do Nothing 789 Brookvale Outlay Plan
• $8,100 – Total Cost $5,525 – Total Cost
• $3,100 – Income Tax $500 fee & $25 GST
• $5,000 – Money needed for medical, dental, vision, etc. $5,000 – Money needed for medical, dental, vision, etc.
• SAVINGS is $2,575
• Assuming a company incorporated in Alberta and a one time setup fee of $275 has not been included in the comparison.
• Information to send us to setup your account is:
• - Names and birth dates of you and your dependents
• - Contact information for you and your business (if different) Address, email, phone numbers
• - We will contact you about how to setup the app, your banking details and some other items.
• - Setup fee is a one-time payment of $275
Nice to have
• I'd like the front of the postcard to not be very busy with the background or graphics, etc. I want the call to action to be very obvious so they want to read the bullet points and look at the back of the postcard for more information.

```html
<!DOCTYPE html>
<html lang="en">
<head>
<meta charset="utf-8">
<title>789 Brookvale Outlay Plan – Postcard</title>
<link href="https://fonts.googleapis.com/css2?family=Open+Sans:ital,wght@0,400;0,600;0,700;0,800;1,400;1,600&display=swap" rel="stylesheet">
<style>
  :root{
    --stage:#2b2b2d;
    --paper:#ffffff;
    --paper-shade:#e9eaec;
    --red:#d6232a;
    --red-dark:#a8161c;
    --blue:#1d6db5;
    --ink:#2a2a2a;
    --muted:#6b6b6b;
    --rule:#c9c9c9;
  }
  *{box-sizing:border-box;margin:0;padding:0}
  html,body{width:874px;height:1200px;overflow:hidden}
  body{background:var(--stage);font-family:'Open Sans',Arial,sans-serif;color:var(--ink);position:relative}
  .card{position:absolute;left:15px;width:844px;height:565px;background:var(--paper);overflow:hidden;box-shadow:0 6px 18px rgba(0,0,0,.5)}
  .card--front{top:15px;background:linear-gradient(180deg,var(--paper-shade) 0%,var(--paper) 40%)}
  .card--back{top:615px}
  .brand{position:absolute;display:flex;align-items:center;gap:12px}
  .brand__mark{width:40px;height:40px;background:var(--red)}
  .brand__name{font-weight:800;font-size:30px;color:var(--red);line-height:1}
  .brand__tag{position:absolute;font-style:italic;font-weight:600;font-size:17px;color:var(--ink);border-top:2px solid var(--ink);padding-top:2px}
  .stamp{position:absolute;right:24px;top:20px;width:86px;height:96px;border:2px solid var(--rule);background:var(--paper)}
  .who{position:absolute;left:26px;top:108px;width:400px}
  .who__title{color:var(--blue);font-weight:700;font-size:21px;line-height:1.2;margin-bottom:8px}
  .who__list{list-style:none;font-size:14.5px;line-height:1.35}
  .who__list li{padding-left:12px;position:relative}
  .who__list li::before{content:"•";position:absolute;left:0}
  .illustration{position:absolute;left:470px;top:132px;width:330px;height:200px;border-radius:6px;background:linear-gradient(160deg,#f3f3f3,#cfd2d6)}
  .alarm{position:absolute;left:0;top:338px;width:100%;height:120px;background:var(--red);border-bottom:8px solid var(--red-dark);padding:12px 26px;display:flex;align-items:center}
  .alarm__text{color:#fff;font-weight:800;font-size:42px;line-height:1.05;letter-spacing:-.5px}
  .footnote{position:absolute;left:26px;top:474px;width:400px;font-style:italic;font-size:17px;line-height:1.3;color:var(--muted)}
  .warning{position:absolute;right:24px;top:466px;width:380px;height:80px;background:var(--blue);color:#fff;font-weight:800;font-size:19px;line-height:1.3;text-align:center;display:flex;align-items:center;justify-content:center;padding:0 16px}
  .col{position:absolute;top:108px}
  .col--left{left:26px;width:398px}
  .col--right{left:446px;width:374px}
  .heading{color:var(--red);font-weight:800;font-size:22px;line-height:1.1;margin-bottom:8px}
  .body{font-size:12.5px;line-height:1.35}
  .sub{color:var(--red);font-weight:800;font-size:17px;text-align:center;margin-top:6px}
  .center{text-align:center}
  .compare{width:100%;border-collapse:collapse;font-size:12px;margin-top:4px}
  .compare th{background:var(--red);color:#fff;font-weight:700;text-align:left;padding:4px 8px;vertical-align:top}
  .compare td{padding:4px 8px;vertical-align:top;border-bottom:1px solid var(--rule)}
  .compare td:first-child{color:var(--red)}
  .savings{color:var(--red);font-weight:800;font-size:17px;text-align:center;margin:6px 0 2px}
  .info__list{list-style:none;font-size:13px;line-height:1.35}
  .info__list li{padding-left:12px;position:relative}
  .info__list li::before{content:"•";position:absolute;left:0}
  .photo{position:absolute;left:470px;top:330px;width:350px;height:215px;background:radial-gradient(ellipse at 55% 65%,#e6e3df 0%,#9c9a98 55%,#4a4a4c 100%)}
  .baseline{position:absolute;left:0;bottom:0;width:100%;height:6px;background:var(--red)}
</style>
</head>
<body>
  <section class="card card--front">
    <div class="brand" style="left:26px;top:22px"><span class="brand__mark"></span><span class="brand__name">789 Brookvale Outlay</span></div>
    <div class="brand__tag" style="left:78px;top:68px">Save Time · Save Money</div>
    <div class="stamp"></div>
    <div class="who">
      <h2 class="who__title">Who should have a<br>789 Brookvale Outlay Plan?</h2>
      <ul class="who__list">
        <li>Every business owner who is incorporated should have one.</li>
        <li>Write off 100% of this QTB approved this method.</li>
        <li>It is the most tax effective way to run dental, health, vision and other expenses through your company.</li>
        <li>Easy to use APP for your phone, 2-day turnaround time for claims</li>
      </ul>
    </div>
    <div class="illustration" role="img" aria-label="Illustration of a businessman seated at a desk with a computer"></div>
    <div class="alarm"><p class="alarm__text">YOU'RE SPENDING<br>TOO MUCH ON TAXES!</p></div>
    <p class="footnote">That's what they'll say if your business doesn't have a 789 Brookvale Outlay Plan...</p>
    <div class="warning">IF YOU AREN'T USING THIS, YOU'RE THROWING TAX DOLLARS AWAY!</div>
  </section>

  <section class="card card--back">
    <div class="brand" style="left:250px;top:22px"><span class="brand__mark"></span><span class="brand__name">789 Brookvale Outlay</span></div>
    <div class="brand__tag" style="left:302px;top:68px">Save Time · Save Money</div>
    <div class="col col--left">
      <h2 class="heading">THE EXAMPLE OF<br>HOW THIS SAVES YOU MONEY:</h2>
      <p class="body">Assuming a 38% personal tax rate. You will need to earn $1.62 of gross income, pay $0.62 of personal tax, which leaves you with $1.00 of after tax money to use for your personal expenses.</p>
      <p class="body">The example of using a 789 Brookvale Outlay Plan, or doing nothing would need the following information.</p>
      <p class="sub">COMPARISON</p>
      <p class="body center">$5,000 of medical, dental, vision expenses</p>
      <table class="compare">
        <tr><th>Do Nothing</th><th>789 Brookvale Outlay Plan</th></tr>
        <tr><td>$3,100 – Income Tax<br>$5,000 – Money needed for medical, dental, vision, etc.</td><td>$500 fee &amp; $25 GST<br>$5,000 – Money needed for medical, dental, vision, etc.</td></tr>
        <tr><td>$8,100 – Total Cost</td><td>$5,525 – Total Cost</td></tr>
      </table>
      <p class="savings">SAVINGS is $2,575</p>
      <p class="body" style="font-size:11.5px">Assuming a company incorporated in Alberta and a one time setup fee of $275 has not been included in the comparison.</p>
    </div>
    <div class="col col--right">
      <h2 class="heading">INFORMATION TO SEND US TO SETUP YOUR ACCOUNT IS:</h2>
      <ul class="info__list">
        <li>Names and birth dates of you and your dependents</li>
        <li>Contact information for you and your business (if different) Address, email, phone numbers</li>
        <li>We will contact you about how to setup the app, your banking details and some other items.</li>
        <li>Setup fee is a one-time payment of $275</li>
      </ul>
    </div>
    <div class="photo" role="img" aria-label="Photo of a hand dropping a coin into a piggy bank beside stacks of coins"></div>
    <div class="baseline"></div>
  </section>
</body>
</html>
```